Thrive Hollow Wording For Logo & Business card

I have the logo, I just need the "thrive Hollow" wording to go with it, and a business card design. The only thing on the business card is the website info. We provide nature connection experiences, and bolster these efforts through writing and host a platform for community around it.

I also have an idea of what it could look like (sketch), though I'm really not sure how it would come out. I am open to the best design and happy to consider original artwork. You can see what the site is about at ThriveHollow.com.

Contact Information for Business Card

The only thing on the business card is the website info and the design. I will put other messaging on the back.

Website lettering (ThriveHollow.com) in Montserrat

Logo Text

Thrive Hollow (letters optional)

Font styles to use
Other font styles liked:
• montserrat

```html
<!DOCTYPE html>
<html lang="en">
<head>
<meta charset="utf-8">
<title>Thrive Hollow – Business Card</title>
<link rel="stylesheet" href="https://fonts.googleapis.com/css2?family=Montserrat:wght@400;500;600&display=swap">
<style>
  :root {
    --stage: #d9d9d9;
    --card-base: #f2f3f1;
    --scene-light: #f4f5f3;
    --scene-mid: #dfe3dc;
    --scene-shade: #c9cfc4;
    --plum: #4e2d6b;
    --plum-soft: #6a4a86;
    --ember: #e98a2a;
    --brand-grey: #6f6f6f;
  }
  * { box-sizing: border-box; margin: 0; padding: 0; }
  html, body { width: 1200px; height: 750px; overflow: hidden; }
  body {
    background: var(--stage);
    font-family: "Montserrat", sans-serif;
    display: flex; align-items: center; justify-content: center;
  }
  .business-card {
    position: relative;
    width: 1000px; height: 571px;
    border-radius: 34px;
    overflow: hidden;
    background: var(--card-base);
  }
  .nature-backdrop {
    position: absolute; inset: 0;
    background:
      radial-gradient(ellipse at 70% 35%, var(--scene-shade) 0%, transparent 55%),
      radial-gradient(ellipse at 40% 80%, var(--scene-mid) 0%, transparent 60%),
      linear-gradient(120deg, var(--scene-light) 0%, var(--scene-mid) 60%, var(--scene-light) 100%);
    opacity: .85;
  }
  .brand-panel {
    position: absolute; left: 0; top: 0; bottom: 0; width: 312px;
    display: flex; flex-direction: column; align-items: center; justify-content: center;
    gap: 26px; padding-top: 80px;
  }
  .brand-disc {
    width: 140px; height: 140px; border-radius: 50%;
    background: var(--plum);
  }
  .brand-name {
    font-size: 28px; font-weight: 500; letter-spacing: 1px;
    color: var(--brand-grey); text-transform: uppercase; white-space: nowrap;
  }
  .divider {
    position: absolute; top: 0; bottom: 0; left: 312px; width: 14px;
    border-left: 5px solid var(--plum);
    border-right: 5px solid var(--plum);
  }
  .edge-band {
    position: absolute; top: 0; bottom: 0; right: 0; width: 22px;
    border-left: 5px solid var(--plum);
    background: linear-gradient(90deg, var(--card-base) 0 6px, var(--plum) 6px);
  }
  .contact-panel {
    position: absolute; left: 326px; top: 0; bottom: 0; right: 22px;
    display: flex; align-items: center; justify-content: center;
  }
  .website {
    display: flex; align-items: center; gap: 18px;
    font-size: 30px; font-weight: 500; color: var(--plum-soft);
  }
  .website-icon { width: 34px; height: 34px; flex: none; }
</style>
</head>
<body>
  <article class="business-card">
    <div class="nature-backdrop" role="img" aria-label="Soft faded photo of a waterfall among forest foliage"></div>

    <section class="brand-panel">
      <div class="brand-disc"></div>
      <p class="brand-name">Thrive Hollow</p>
    </section>

    <div class="divider"></div>

    <section class="contact-panel">
      <p class="website">
        <svg class="website-icon" viewBox="0 0 24 24" aria-hidden="true">
          <circle cx="12" cy="12" r="11" fill="var(--ember)"/>
          <g fill="none" stroke="#fff" stroke-width="1.4">
            <ellipse cx="12" cy="12" rx="4.5" ry="10"/>
            <line x1="2" y1="12" x2="22" y2="12"/>
            <path d="M4 7h16M4 17h16"/>
          </g>
        </svg>
        www.thrivehollow.com
      </p>
    </section>

    <div class="edge-band"></div>
  </article>
</body>
</html>
```